Company Proposal Powerpoint Template

We would like to update our overall proposal presentation with a fresh, new look that might appeal to the younger generation. We are a full-meeting management company that specializes in corporate events sales meetings, incentive trips, and tradeshows/conferences.
We have a core set of slides that we use for presentations, but will also need to customize based on the customers we service and what we are selling each potential client.
We have a company logo, but we are not tied into the colors schemes for the logo and are okay adding the logo in black or white versus in color.
I have included our current look and feel for this presentation. This will also give you content that we typically add to this presentation.
Reason: Traveling out of the office so limited access to review the art.
Industry/Entity Type
It Company
Look and feel
Each slider illustrates characteristics of the customer's brand and the style your logo design should communicate.

```html
<!DOCTYPE html>
<html lang="en">
<head>
<meta charset="utf-8">
<title>Kestrel One – Proposal Slide Set</title>
<link href="https://fonts.googleapis.com/css2?family=Open+Sans:wght@300;400;600;700&display=swap" rel="stylesheet">
<style>
:root{
  --red:#e0123f;
  --pink:#f8557f;
  --deep:#c40c3a;
  --ink:#6b6b6b;
  --ink-dark:#4f4f4f;
  --grey-box:#8f8f8f;
  --brand:#7a7468;
  --white:#ffffff;
  --paper:#ffffff;
  --slide-grad:linear-gradient(125deg,#d20d3b 0%,#ec1b50 30%,#ff6a8e 52%,#ef2257 72%,#cf0c3a 100%);
}
*{box-sizing:border-box;margin:0;padding:0}
html,body{width:1200px;height:1000px;overflow:hidden;background:#fff}
body{font-family:"Open Sans",Arial,sans-serif;color:var(--ink)}
.canvas{position:relative;width:1200px;height:1000px;overflow:hidden;background:#fff}

.slide{position:absolute;background:var(--slide-grad);box-shadow:3px 3px 5px rgba(0,0,0,.55);overflow:hidden}
.sheet{position:absolute;left:8px;right:8px;top:8px;bottom:20px;background:var(--paper)}
.head{position:absolute;left:0;right:0;top:8px;height:24px;background:var(--paper)}
.slide-title{position:absolute;left:10px;top:7px;font-size:10px;font-weight:400;letter-spacing:.5px;text-transform:uppercase;color:var(--ink)}

.brand{position:absolute;display:flex;align-items:center;gap:3px;color:var(--brand);font-weight:400;white-space:nowrap}
.brand-dot{display:inline-block;border-radius:50%;background:var(--red)}
.brand--sm{right:8px;top:6px;font-size:8px}
.brand--sm .brand-dot{width:8px;height:8px}

.photo{position:absolute}
.avatar{position:absolute;border-radius:50%;border:2px solid #fff;box-shadow:0 0 0 1px #ddd;background:radial-gradient(circle at 50% 40%,#d9b48c,#8a5a3a)}

/* intro partial */
.intro-panel{position:absolute;left:0;right:8px;top:15px;height:78px;background:var(--paper)}
.intro-text{position:absolute;top:12px;font-size:6.5px;line-height:1.35;color:var(--ink-dark)}

/* full service */
.fs-box{position:absolute;left:0;width:74px;background:var(--paper);font-size:4.4px;line-height:1.25;padding:3px 3px;color:var(--ink-dark)}
.fs-box b{display:block;font-size:5.2px;color:var(--ink-dark)}

/* title slide */
.cover-band{position:absolute;left:0;right:0;top:90px;height:135px;background:var(--paper)}
.cover-date{position:absolute;top:10px;width:100%;text-align:center;font-size:14px;font-weight:300;color:var(--ink)}
.cover-brand{left:70px;top:50px;font-size:40px;font-weight:300;gap:12px}
.cover-brand .brand-dot{width:34px;height:34px}
.cover-client{position:absolute;top:235px;width:100%;text-align:center;color:var(--white);font-size:14px;letter-spacing:1px;font-weight:300}

/* toc */
.toc{position:absolute;left:36px;top:42px;list-style:none}
.toc li{display:flex;align-items:center;gap:7px;height:21px;font-size:10px;color:var(--ink)}
.toc-num{width:16px;height:16px;border-radius:50%;background:var(--red);color:#fff;font-size:8px;display:flex;align-items:center;justify-content:center;font-weight:600}

/* overview */
.overview-text{position:absolute;left:10px;top:50px;width:112px;font-size:6.2px;font-weight:700;line-height:1.35;color:var(--ink-dark)}
.overview-text p{margin-bottom:7px}
.overview-text ul{list-style:none;padding-left:8px}
.overview-text li::before{content:"✓ ";}

/* team */
.team-lead{position:absolute;font-size:6.5px;color:var(--ink)}
.team-lead b{font-weight:700}
.team-rule{position:absolute;height:1px;background:#bbb}
.member{position:absolute;display:flex;align-items:center;gap:5px;font-size:6px;line-height:1.25;color:var(--ink)}
.member .avatar{position:static;width:24px;height:24px;flex:none}
.bio{position:absolute;left:8px;right:8px;font-size:4.6px;line-height:1.3;color:#666;text-align:justify}
.bio p{margin-bottom:4px}

/* who */
.who-lead{position:absolute;left:18px;top:58px;font-size:6.5px;font-weight:700;color:var(--ink-dark)}
.who-col{position:absolute;top:76px;width:76px;height:94px;background:var(--grey-box);color:#fff;font-size:5.6px;line-height:1.25;padding:4px 4px 4px 16px}
.who-col p{margin-bottom:4px}
.who-label{position:absolute;left:2px;bottom:4px;transform-origin:left bottom;transform:rotate(-90deg) translate(0,10px);font-size:5.5px;white-space:nowrap;width:90px}
.who-arrow{position:absolute;top:160px;width:0;height:0;border-top:6px solid transparent;border-bottom:6px solid transparent;border-left:7px solid #fff}

/* air */
.air-lead{position:absolute;left:10px;top:48px;width:58px;font-size:6.4px;font-weight:700;line-height:1.35;color:var(--ink-dark)}
.air-lead p{margin-bottom:8px}
.air-col{position:absolute;top:38px;width:64px;text-align:center;font-size:4.9px;line-height:1.3;color:var(--ink-dark)}
.air-col b{display:block;font-size:5.4px;margin:3px 0 1px}
.air-icon{display:block;margin:0 auto;width:15px;height:15px}

/* online reg */
.reg-list{position:absolute;left:10px;top:32px;list-style:none;color:#fff;font-size:6.3px;font-weight:700;line-height:1.55}
.reg-list .sub{font-weight:400;padding-left:12px;font-size:5.6px;line-height:1.4}
.badge{position:absolute;background:var(--paper);border-radius:3px}

/* reg services */
.rs-band{position:absolute;left:83px;right:0;top:90px;height:22px;background:var(--paper)}
.rs-band span{position:absolute;left:10px;top:5px;font-size:9px;color:var(--ink);letter-spacing:.5px}
.rs-brand{left:92px;top:124px;font-size:15px;color:#fff}
.rs-brand .brand-dot{width:12px;height:12px;background:#fff}

/* portfolio */
.client{position:absolute;font-size:8px;font-weight:700;color:var(--ink-dark);white-space:nowrap}

/* contact */
.contact-top{position:absolute;left:0;right:0;top:0;height:10px;background:var(--slide-grad)}
.contact{position:absolute;left:8px;top:74px;font-size:7.5px;line-height:1.45;color:var(--ink)}
.contact h3{font-size:8.5px;font-weight:400;letter-spacing:.5px;margin-bottom:3px}

/* data management */
.dm-head{position:absolute;left:0;right:0;top:14px;height:36px;background:var(--paper)}
.dm-title{position:absolute;left:22px;top:7px;font-size:16px;font-weight:400;letter-spacing:.8px;color:var(--ink)}
.dm-brand{right:14px;top:9px;font-size:13px}
.dm-brand .brand-dot{width:14px;height:14px}
.dm-lead{position:absolute;left:16px;top:64px;width:192px;color:#fff;font-size:10.6px;font-weight:700;line-height:14px;letter-spacing:-.1px}
.dm-panel{position:absolute;left:12px;top:152px;width:416px;height:172px;background:var(--paper)}
.dm-panel h3{position:absolute;left:10px;top:18px;font-size:10.5px;font-weight:600;color:var(--ink)}
.dm-item{position:absolute;display:flex;gap:10px;font-size:9.6px;line-height:1.35;color:var(--ink)}
.dm-item svg{flex:none;width:20px;height:20px;margin-top:1px}
</style>
</head>
<body>
<div class="canvas">

  <!-- Intro partial -->
  <section class="slide" style="left:-100px;top:-8px;width:272px;height:113px">
    <div class="intro-panel" style="left:100px">
      <p class="intro-text" style="left:0;width:74px">From conferences to incentive trips, keep attendance high with the right “look” to your program</p>
      <p class="intro-text" style="left:86px;width:74px">K1’s web team will take your graphics and design a fully-customized website to keep your attendees informed</p>
    </div>
  </section>

  <!-- Full service -->
  <section class="slide" style="left:-100px;top:112px;width:270px;height:193px">
    <div class="sheet" style="left:100px;right:0;top:8px;bottom:auto;height:30px">
      <div class="brand brand--sm"><span class="brand-dot"></span>Kestrel One</div>
    </div>
    <div class="head" style="left:100px;top:42px;height:16px"><span class="slide-title" style="left:0;top:2px;font-size:8.5px">Full Service Meeting Solution</span></div>
    <div class="fs-box" style="left:100px;top:66px;height:60px"><b>REGISTRATION SERVICES</b>Website Design &amp; Development. Online Registration Turnkey Services; Licensed Platforms to Select from; Housing/Registration Management, including call centers</div>
    <div class="fs-box" style="left:100px;top:130px;height:52px"><b>ONSITE EVENT MANAGEMENT</b>Informed, Resourceful and Experienced On-Site Staff available 24/7 while on-site</div>
    <svg style="position:absolute;left:180px;top:62px" width="84" height="124" viewBox="0 0 84 124">
      <path d="M30 20 A40 40 0 0 1 62 50" fill="none" stroke="#9a9a9a" stroke-width="7"/>
      <path d="M62 70 A40 40 0 0 1 30 100" fill="none" stroke="#9a9a9a" stroke-width="7"/>
      <path d="M22 96 A40 40 0 0 1 22 30" fill="none" stroke="#b5b5b5" stroke-width="6"/>
      <circle cx="32" cy="20" r="16" fill="#e0123f" stroke="#fff" stroke-width="1.5"/>
      <circle cx="52" cy="60" r="16" fill="#e0123f" stroke="#fff" stroke-width="1.5"/>
      <circle cx="32" cy="102" r="16" fill="#e0123f" stroke="#fff" stroke-width="1.5"/>
      <g fill="#fff" font-family="Open Sans, sans-serif" font-size="3.6" text-anchor="middle" font-weight="700">
        <text x="32" y="18">ONSITE EVENT</text><text x="32" y="23">MANAGEMENT</text>
        <text x="52" y="56">EVENT</text><text x="52" y="61">MANAGEMENT</text><text x="52" y="66">SERVICES</text>
        <text x="32" y="101">REGISTRATION</text><text x="32" y="106">SERVICES</text>
      </g>
    </svg>
  </section>

  <!-- Cover -->
  <section class="slide" style="left:193px;top:8px;width:420px;height:310px">
    <div class="cover-band">
      <p class="cover-date">DATE</p>
      <div class="brand cover-brand"><span class="brand-dot"></span>Kestrel One</div>
    </div>
    <p class="cover-client">NAME OF THE CUSTOMER</p>
  </section>

  <!-- Table of content -->
  <section class="slide" style="left:617px;top:8px;width:276px;height:199px">
    <div class="sheet">
      <span class="slide-title">Table of Content</span>
      <div class="brand brand--sm"><span class="brand-dot"></span>Kestrel One</div>
      <ol class="toc">
        <li><span class="toc-num">1</span>Name of part 1</li>
        <li><span class="toc-num">2</span>Name of part 2</li>
        <li><span class="toc-num">3</span>Name of part 3</li>
        <li><span class="toc-num">4</span>Name of part 4</li>
        <li><span class="toc-num">5</span>Name of part 5</li>
      </ol>
    </div>
  </section>

  <!-- Company overview -->
  <section class="slide" style="left:903px;top:8px;width:272px;height:199px">
    <div class="sheet" style="right:0;bottom:0">
      <span class="slide-title">Company Overview</span>
      <div class="brand brand--sm"><span class="brand-dot"></span>Kestrel One</div>
      <div class="overview-text">
        <p>Formed 4 years after KG (1996) as a Direct Response to our Clients’ Needs</p>
        <p>One Stop Shopping</p>
        <p>As Former Clients, our mission is to provide what we always wanted:</p>
        <ul><li>Staff with Experience</li><li>Outstanding Value</li><li>The Real Magic - Customized Service</li></ul>
      </div>
    </div>
    <div class="photo" role="img" aria-label="Photo of the company headquarters building at dusk" style="left:130px;top:28px;right:0;bottom:0;background:linear-gradient(160deg,#3f5f96 0%,#6f86ad 45%,#c6a06c 80%,#5a4a36 100%)"></div>
  </section>

  <!-- Team grid -->
  <section class="slide" style="left:617px;top:215px;width:276px;height:205px">
    <div class="sheet">
      <span class="slide-title">Your K1 Team</span>
      <div class="brand brand--sm"><span class="brand-dot"></span>Kestrel One</div>
      <div class="avatar" role="img" aria-label="Portrait of Dana Whitfield" style="left:164px;top:24px;width:52px;height:52px"></div>
      <p class="team-lead" style="left:22px;top:64px"><b>Dana Whitfield,</b> Vice President</p>
      <div class="team-rule" style="left:18px;top:76px;width:150px"></div>
      <div class="member" style="left:22px;top:96px"><span class="avatar" role="img" aria-label="Portrait of Owen Marsh"></span><span><b>Owen Marsh,</b> Director<br>of Technology</span></div>
      <div class="member" style="left:132px;top:96px"><span class="avatar" role="img" aria-label="Portrait of Lena Hart"></span><span><b>Lena Hart,</b> Director<br>Global Sales</span></div>
      <div class="member" style="left:22px;top:134px"><span class="avatar" role="img" aria-label="Portrait of Mira Cole"></span><span><b>Mira Cole,</b> Director of<br>Operations</span></div>
      <div class="member" style="left:132px;top:134px"><span class="avatar" role="img" aria-label="Portrait of Tess Rowan"></span><span><b>Tess Rowan,</b> Sales</span></div>
    </div>
  </section>

  <!-- Bio Dana -->
  <section class="slide" style="left:903px;top:215px;width:272px;height:205px">
    <div class="sheet">
      <span class="slide-title">Your K1 Team</span>
      <div class="brand brand--sm"><span class="brand-dot"></span>Kestrel One</div>
      <div class="avatar" role="img" aria-label="Portrait of Dana Whitfield" style="left:194px;top:22px;width:48px;height:48px"></div>
      <p class="team-lead" style="left:52px;top:64px"><b>Dana Whitfield,</b> Vice President</p>
      <div class="team-rule" style="left:8px;top:76px;width:240px"></div>
      <div class="bio" style="top:82px">
        <p>Dana leads daily operations of the meetings division, guiding strategy, business growth and the sales team. She shapes brand identity, builds client relationships and oversees planning for programs of every size. Before joining in 2009, she directed global events for a large technology firm, running sales conferences, product launches, incentive trips and hospitality events for up to five thousand guests.</p>
        <p>She has managed film festivals, golf tournaments, tennis finals and motor racing weekends, and she studied at two universities in Texas. She is based in Dallas.</p>
      </div>
    </div>
  </section>

  <!-- Who is -->
  <section class="slide" style="left:52px;top:343px;width:270px;height:202px">
    <div class="sheet">
      <span class="slide-title">Who is K1?</span>
      <div class="brand brand--sm"><span class="brand-dot"></span>Kestrel One</div>
      <p class="who-lead" style="left:10px">Full Meetings Management Division of Kestrel Group</p>
      <div class="who-col" style="left:10px"><span class="who-label">Corporate Meetings</span><p>Annual Meetings, Sales &amp; Marketing Meetings</p><p>CEO Summits/Board of Director’s Meetings</p><p>Investigator Meetings / Board Meetings</p><p>Client &amp; Hospitality Events</p></div>
      <div class="who-arrow" style="left:86px"></div>
      <div class="who-col" style="left:90px"><span class="who-label">Incentive Programs</span><p>Sales Incentive Programs</p><p>Weekend Incentive Programs</p><p>Incentive Trips</p><p>Domestic &amp; International</p></div>
      <div class="who-arrow" style="left:166px"></div>
      <div class="who-col" style="left:170px"><span class="who-label">Conferences &amp; Tradeshows</span><p>Multi-track Conferences</p><p>50 Attendees - 6000+ Attendees</p><p>Education &amp; Training</p></div>
    </div>
  </section>

  <!-- Tradeshows -->
  <section class="slide" style="left:336px;top:343px;width:269px;height:202px">
    <div class="head"><span class="slide-title">Tradeshows</span><div class="brand brand--sm"><span class="brand-dot"></span>Kestrel One</div></div>
    <div class="photo" role="img" aria-label="Photo of a busy tradeshow floor" style="left:8px;top:38px;width:90px;height:62px;background:linear-gradient(135deg,#3a5b8c,#9aa7b8)"></div>
    <div class="photo" role="img" aria-label="Photo of a team at an exhibit booth" style="left:103px;top:38px;width:68px;height:62px;background:linear-gradient(135deg,#2a4a86,#c9c2b0)"></div>
    <div class="photo" role="img" aria-label="Photo of an outdoor exhibit stand" style="left:176px;top:38px;width:85px;height:62px;background:linear-gradient(135deg,#8fb2d6,#6f6f6f)"></div>
    <div class="photo" role="img" aria-label="Photo of a large branded exhibition hall" style="left:8px;top:105px;width:178px;height:88px;background:linear-gradient(135deg,#e8e2d6,#c8342f 60%,#d9d4c8)"></div>
    <div class="photo" role="img" aria-label="Photo of a speaker on a conference stage" style="left:191px;top:105px;width:70px;height:88px;background:linear-gradient(135deg,#1e2a4a,#b85a2a)"></div>
  </section>

  <!-- Bio Lena -->
  <section class="slide" style="left:617px;top:428px;width:276px;height:200px">
    <div class="sheet">
      <span class="slide-title">Your K1 Team</span>
      <div class="avatar" role="img" aria-label="Portrait of Lena Hart" style="left:196px;top:22px;width:48px;height:48px"></div>
      <p class="team-lead" style="left:62px;top:66px"><b>Lena Hart,</b> director, global sales</p>
      <div class="team-rule" style="left:8px;top:77px;width:244px"></div>
      <div class="bio" style="top:82px">
        <p>Lena joined the company in 2012 as director of global sales. With twenty years in the event industry, her passion for service and strong client care help the team reach new markets.</p>
        <p>Before this role, she spent nine years leading corporate meetings for a national retailer, from store manager conferences and incentive programs to charity fundraisers and board meetings for up to four thousand guests. She also ran a large in-house function space, then worked with planners across many industries on tournaments, trade shows and franchise conferences. She serves on the boards of several nonprofit groups and lives in Dallas.</p>
      </div>
    </div>
  </section>

  <!-- Bio Mira -->
  <section class="slide" style="left:903px;top:428px;width:272px;height:200px">
    <div class="sheet">
      <span class="slide-title">Your K1 Team</span>
      <div class="brand brand--sm"><span class="brand-dot"></span>Kestrel One</div>
      <div class="avatar" role="img" aria-label="Portrait of Mira Cole" style="left:196px;top:22px;width:48px;height:48px"></div>
      <p class="team-lead" style="left:58px;top:66px"><b>Mira Cole,</b> senior director, operations</p>
      <div class="team-rule" style="left:8px;top:77px;width:240px"></div>
      <div class="bio" style="top:82px">
        <p>Mira joined the company in 2003. After two years of operations work she moved into sales, managing several territories and a number of clients. She now heads the operations team, handling staff, training, contracts and financial oversight. She began her career in Southern California in 1996, then planned large events for an imaging company and a national bank, from sales meetings and kickoffs to incentive trips, road shows and celebrity golf events. She holds a degree in political science and lives in Dallas.</p>
      </div>
    </div>
  </section>

  <!-- Air ticketing -->
  <section class="slide" style="left:52px;top:553px;width:270px;height:202px">
    <div class="sheet">
      <span class="slide-title">Air Ticketing Services</span>
      <div class="brand brand--sm"><span class="brand-dot"></span>Kestrel One</div>
      <div class="air-lead"><p>K1 delivers start-to-finish air fulfillment and management of group air services.</p><p>Typical service offerings:</p></div>
      <div class="air-col" style="left:64px">
        <svg class="air-icon" viewBox="0 0 16 16"><circle cx="8" cy="8" r="8" fill="#e0123f"/><rect x="4" y="5" width="8" height="6" fill="none" stroke="#fff" stroke-width="1"/><line x1="4" y1="7" x2="12" y2="7" stroke="#fff" stroke-width="1"/></svg>
        <b>Group Air Reservations</b>air ticketing, consultation, air lift analysis, airline negotiations &amp; contracting, block space coordination, international and domestic expertise. 24-hour emergency service
      </div>
      <div class="air-col" style="left:128px">
        <svg class="air-icon" viewBox="0 0 16 16"><circle cx="8" cy="8" r="8" fill="#e0123f"/><path d="M8 3.5l1.3 2.8 3 .3-2.3 2 .7 3-2.7-1.6-2.7 1.6.7-3-2.3-2 3-.3z" fill="none" stroke="#fff" stroke-width=".9"/></svg>
        <b>Management Assistance</b>partner to set program goals and workable air budgets, define optimal air procedures
      </div>
      <div class="air-col" style="left:190px">
        <svg class="air-icon" viewBox="0 0 16 16"><circle cx="8" cy="8" r="8" fill="#e0123f"/><path d="M5 11h6l-1-2V7a2 2 0 0 0-4 0v2z" fill="none" stroke="#fff" stroke-width=".9"/><circle cx="8" cy="12.3" r=".8" fill="#fff"/></svg>
        <b>Value Added Services</b>on-site air agent support, upgrade and waitlist processing, VIP &amp; concierge services, in-flight attendee tracking system, budget consultation, assistance with documents and visa/passport services
      </div>
    </div>
  </section>

  <!-- Online registration -->
  <section class="slide" style="left:336px;top:553px;width:269px;height:202px">
    <div class="head"><span class="slide-title">Online Registration</span><div class="brand brand--sm"><span class="brand-dot"></span>Kestrel One</div></div>
    <ul class="reg-list">
      <li>Not Just Registration Anymore</li>
      <li>Plan, Market, Manage, &amp; Execute Your Events</li>
      <li class="sub">Highlights: eSurvey, eBudget, eScheduler, eSeating, eBooth, eMobile</li>
      <li class="sub">Hot trend: Mobile Apps</li>
      <li>Connection to Online Air Ticketing</li>
      <li>Supported in 26 Languages</li>
      <li>PCI-Level 1 Compliant</li>
      <li>Interactive Demo</li>
    </ul>
    <div class="photo" role="img" aria-label="Screenshot of an event registration page" style="left:180px;top:62px;width:44px;height:62px;background:linear-gradient(180deg,#f4f4f4,#d8dde6)"></div>
    <div class="photo" role="img" aria-label="Screenshot of a registration form" style="left:215px;top:56px;width:46px;height:52px;background:linear-gradient(180deg,#fafafa,#e2e6ec)"></div>
    <div class="badge" style="left:10px;top:138px;width:46px;height:12px"></div>
    <div class="badge" style="left:64px;top:138px;width:40px;height:12px"></div>
    <div class="photo" role="img" aria-label="Screenshot of an event planning timeline" style="left:10px;top:154px;width:160px;height:40px;background:linear-gradient(180deg,#ffffff,#dfe4ec)"></div>
    <div class="photo" role="img" aria-label="Screenshot of a seating chart tool" style="left:180px;top:132px;width:80px;height:62px;background:linear-gradient(135deg,#f6f6f6,#c9c6e6)"></div>
  </section>

  <!-- Registration services divider -->
  <section class="slide" style="left:52px;top:767px;width:270px;height:203px">
    <div class="rs-band"><span>REGISTRATION SERVICES</span></div>
    <div class="brand rs-brand"><span class="brand-dot"></span>Kestrel One</div>
  </section>

  <!-- Sales meetings -->
  <section class="slide" style="left:336px;top:770px;width:269px;height:200px">
    <div class="head"><span class="slide-title">Sales Meetings &amp; Conferences</span><div class="brand brand--sm"><span class="brand-dot"></span>Kestrel One</div></div>
    <div class="photo" role="img" aria-label="Photo of a packed banquet hall" style="left:8px;top:35px;width:125px;height:80px;background:linear-gradient(135deg,#2a1e16,#7a4a2a 60%,#1c1410)"></div>
    <div class="photo" role="img" aria-label="Photo of a presenter on a bright conference stage" style="left:138px;top:35px;width:123px;height:80px;background:linear-gradient(135deg,#bfe6ee,#ffffff 50%,#9fd0dc)"></div>
    <div class="photo" role="img" aria-label="Photo of a crowd at an evening event" style="left:8px;top:122px;width:90px;height:70px;background:linear-gradient(135deg,#4a3a8a,#c07aa8)"></div>
    <div class="photo" role="img" aria-label="Photo of a large stage with screens" style="left:102px;top:122px;width:78px;height:70px;background:linear-gradient(135deg,#1a2a5a,#6a8ac8)"></div>
    <div class="photo" role="img" aria-label="Photo of a themed party setting" style="left:184px;top:122px;width:77px;height:70px;background:linear-gradient(135deg,#5a1a1a,#e0604a)"></div>
  </section>

  <!-- Customer portfolio -->
  <section class="slide" style="left:617px;top:640px;width:276px;height:200px">
    <div class="sheet">
      <span class="slide-title">Customer Portfolio</span>
      <span class="client" style="left:6px;top:42px;font-size:11px">Norvik</span>
      <span class="client" style="left:70px;top:44px">Treadline</span>
      <span class="client" style="left:6px;top:70px">Voltaro</span>
      <span class="client" style="left:56px;top:68px">Brightwell</span>
      <span class="client" style="left:56px;top:90px">Frostline</span>
      <span class="client" style="left:6px;top:116px;font-size:10px">Polyden</span>
      <span class="client" style="left:70px;top:116px">Imvara</span>
      <span class="client" style="left:6px;top:140px;font-size:6px">Roadmax</span>
      <span class="client" style="left:50px;top:136px;font-size:10px">Fresco Foods</span>
      <span class="client" style="left:6px;top:160px;font-size:6.5px">Lumiskin</span>
    </div>
  </section>

  <!-- Contact -->
  <section class="slide" style="left:617px;top:857px;width:268px;height:150px;background:var(--paper)">
    <div class="contact-top"></div>
    <div class="contact">
      <h3>YOUR CONTACT</h3>
      <p>Name</p><p>Address</p><p>Phone</p><p>Email</p>
    </div>
  </section>

  <!-- Data management -->
  <section class="slide" style="left:735px;top:633px;width:440px;height:332px">
    <div class="dm-head">
      <span class="dm-title">DATA MANAGEMENT &amp; CALL CENTER</span>
      <div class="brand dm-brand"><span class="brand-dot"></span>Kestrel One</div>
    </div>
    <p class="dm-lead">After your website launches, your event registrar will be the point of contact for all questions pertaining to registration and the overall event.</p>
    <div class="photo" role="img" aria-label="Photo of call center agents wearing headsets" style="left:212px;top:62px;width:211px;height:128px;background:linear-gradient(120deg,#f4f1ee,#e6d6c8 45%,#b9a08c 70%,#f2efec)"></div>
    <div class="dm-panel">
      <h3>Registrar Services</h3>
      <div class="dm-item" style="left:18px;top:56px;width:190px">
        <svg viewBox="0 0 20 20"><circle cx="10" cy="10" r="9" fill="none" stroke="#e0123f" stroke-width="1.5"/><path d="M10 5v5l3 2" fill="none" stroke="#e0123f" stroke-width="1.5"/></svg>
        <span>Available during business hours daily leading up to event</span>
      </div>
      <div class="dm-item" style="left:18px;top:98px;width:190px">
        <svg viewBox="0 0 20 20"><circle cx="10" cy="10" r="9" fill="none" stroke="#e0123f" stroke-width="1.5"/><rect x="7" y="5" width="6" height="10" rx="3" fill="none" stroke="#e0123f" stroke-width="1.3"/><line x1="10" y1="6.5" x2="10" y2="9" stroke="#e0123f" stroke-width="1.3"/></svg>
        <span>Full-access to online registration system in order to assist and edit registrations, look-up information, and answer questions</span>
      </div>
      <div class="dm-item" style="left:216px;top:56px;width:190px">
        <svg viewBox="0 0 20 20"><circle cx="10" cy="10" r="9" fill="none" stroke="#e0123f" stroke-width="1.5"/><circle cx="9" cy="9" r="3.5" fill="none" stroke="#e0123f" stroke-width="1.4"/><line x1="11.5" y1="11.5" x2="14.5" y2="14.5" stroke="#e0123f" stroke-width="1.6"/></svg>
        <span>Coordination of rooming list with the hotel – watch room block and pick-up</span>
      </div>
      <div class="dm-item" style="left:216px;top:98px;width:190px">
        <svg viewBox="0 0 20 20"><circle cx="10" cy="10" r="9" fill="none" stroke="#e0123f" stroke-width="1.5"/><circle cx="10" cy="10.5" r="4.5" fill="none" stroke="#e0123f" stroke-width="1.3"/><path d="M10 8v2.5l1.8 1.2" fill="none" stroke="#e0123f" stroke-width="1.2"/></svg>
        <span>Customized reporting and lists to client</span>
      </div>
    </div>
  </section>

</div>
</body>
</html>
```